Website Page Design for Velmont Microbrewery

We need a website page design for our brewery based on our logo and label.

Industry/Entity Type

Brewery

```html
<!DOCTYPE html>
<html lang="pt">
<head>
<meta charset="utf-8">
<title>Velmont Microbrewery – Cerveja Artesanal</title>
<link href="https://fonts.googleapis.com/css2?family=Oswald:wght@500;700&family=Open+Sans:wght@400;600&display=swap" rel="stylesheet">
<style>
  :root{
    --gold:#ffb400;
    --gold-deep:#f39c00;
    --nav-text:#8a2a06;
    --wood-dark:#2a170b;
    --wood-mid:#5e3a1d;
    --wood-light:#8a5c33;
    --plank-line:rgba(0,0,0,.28);
    --white:#ffffff;
    --form-band:rgba(150,45,20,.72);
    --footer:#5a2412;
  }
  *{margin:0;padding:0;box-sizing:border-box}
  html,body{width:848px;height:1200px;overflow:hidden}
  body{
    position:relative;
    font-family:"Open Sans",sans-serif;
    color:var(--white);
    background:
      radial-gradient(ellipse at 50% 40%, rgba(255,200,140,.18), transparent 60%),
      linear-gradient(90deg, var(--wood-dark) 0%, var(--wood-mid) 20%, var(--wood-light) 50%, var(--wood-mid) 80%, var(--wood-dark) 100%);
  }
  .site-header{position:absolute;left:0;top:25px;width:848px;height:33px;
    background:linear-gradient(180deg,#ffd23a,var(--gold) 60%,var(--gold-deep));
    box-shadow:0 2px 6px rgba(0,0,0,.5)}
  .brand{position:absolute;left:29px;top:-14px;width:146px;height:60px;display:flex;align-items:center;gap:7px}
  .brand-dot{width:14px;height:14px;border-radius:50%;background:var(--wood-dark)}
  .brand-name{font-family:"Oswald",sans-serif;font-weight:700;font-size:28px;color:var(--wood-dark);letter-spacing:.5px}
  .main-nav{position:absolute;left:229px;top:0;height:33px;display:flex;align-items:center;gap:23px}
  .main-nav a{font-family:"Oswald",sans-serif;font-weight:500;font-size:13.5px;color:var(--nav-text);text-decoration:none;text-transform:uppercase;letter-spacing:.2px}
  .main-nav a.active{color:var(--white)}
  .social{position:absolute;left:768px;top:5px;display:flex;gap:8px}
  .social span{width:22px;height:22px;border-radius:50%;background:#2a7fd8;border:2px solid var(--white)}

  .heading-xl{font-family:"Oswald",sans-serif;font-weight:700;color:var(--gold);text-transform:uppercase;line-height:1;text-shadow:2px 3px 4px rgba(0,0,0,.6)}
  .hero-title{position:absolute;left:56px;top:160px;font-size:66px}
  .hero-sub{position:absolute;left:57px;top:236px;font-size:30px}
  .body-copy{font-size:10.6px;line-height:12.9px;letter-spacing:.15px;text-shadow:0 1px 2px rgba(0,0,0,.6)}
  .hero-copy{position:absolute;left:58px;top:288px;width:400px}
  .more-link{font-family:"Oswald",sans-serif;font-weight:500;font-size:12.5px;color:var(--white);text-transform:uppercase;text-decoration:underline;text-underline-offset:3px}
  .hero-actions{position:absolute;left:58px;top:402px;display:flex;align-items:center;gap:18px}
  .like-btn{display:flex;align-items:center;gap:4px}
  .like-btn b{background:#3b5998;color:var(--white);font-size:9px;font-weight:600;padding:2px 5px;border-radius:2px}
  .like-btn i{font-style:normal;background:var(--white);color:#333;font-size:8.5px;padding:1px 3px;border:1px solid #bbb;border-radius:2px}

  .bottles{position:absolute;left:513px;top:54px;width:315px;height:580px;border-radius:90px 90px 40px 40px;
    background:radial-gradient(ellipse at 55% 55%, #d9781c 0%, #8a3f0c 55%, rgba(60,25,5,0) 78%)}
  .wheat-left{position:absolute;left:0;top:422px;width:323px;height:290px;border-radius:50%;
    background:radial-gradient(ellipse at 40% 50%, rgba(222,165,95,.75), rgba(222,165,95,0) 70%)}
  .wheat-right{position:absolute;left:770px;top:778px;width:78px;height:141px;
    background:radial-gradient(ellipse at 70% 50%, rgba(222,165,95,.7), rgba(222,165,95,0) 72%)}

  .video{position:absolute;left:55px;top:618px;width:328px;height:218px;border:2px solid var(--white);background:#111}
  .video-frame{position:absolute;inset:0 0 14px 0;
    background:radial-gradient(circle at 32% 55%, #e59a2a 0%, #9b5a18 28%, #3e2413 60%, #1b0f08 100%)}
  .play{position:absolute;left:131px;top:74px;width:74px;height:52px;border-radius:12px;background:rgba(40,40,40,.9)}
  .video-bar{position:absolute;left:0;right:0;bottom:0;height:14px;background:#1a1a1a;display:flex;align-items:center;gap:6px;padding:0 6px;font-size:5px;color:#ccc}

  .feature-title{position:absolute;left:405px;top:631px;font-size:45px}
  .feature-sub{position:absolute;left:406px;top:680px;font-size:21px}
  .feature-copy{position:absolute;left:406px;top:719px;width:424px}
  .feature-more{position:absolute;left:408px;top:801px}

  .contact-title{position:absolute;left:225px;top:903px;font-size:44px}
  .label-title{font-family:"Oswald",sans-serif;font-weight:700;color:var(--gold);text-transform:uppercase;font-size:19px;line-height:1;text-shadow:1px 2px 3px rgba(0,0,0,.6)}
  .enquiry{position:absolute;left:229px;top:956px}
  .glasses{position:absolute;left:62px;top:944px;width:141px;height:236px;border-radius:18px 18px 10px 10px;
    background:linear-gradient(180deg,#fbf4e2 0%,#fbf4e2 12%,#f3b739 20%,#d98a12 70%,#b86a0a 100%)}
  .enquiry-form{position:absolute;left:228px;top:985px;width:302px}
  .field{display:block;background:var(--form-band);font-size:10.5px;padding:7px 8px;margin-bottom:5px}
  .field.name{height:36px}
  .field.email{height:38px}
  .field.comment{height:56px}
  .contact-info{position:absolute;left:567px;top:959px;width:200px}
  .contact-info p{font-size:10.5px;line-height:12.9px;letter-spacing:.2px;margin:3px 0 14px}
  .bottle-cap{position:absolute;left:749px;top:1105px;width:78px;height:72px;border-radius:50%;
    background:radial-gradient(circle at 40% 40%, #f4ebc7, #c9b67a 70%, #8e7a45)}
  .site-footer{position:absolute;left:0;top:1155px;width:848px;height:45px;background:linear-gradient(180deg,#7a331a,var(--footer))}
  .copyright{position:absolute;left:619px;top:9px;font-size:9px}
</style>
</head>
<body>
  <header class="site-header">
    <div class="brand"><span class="brand-dot"></span><span class="brand-name">Velmont</span></div>
    <nav class="main-nav">
      <a class="active" href="#">Início</a>
      <a href="#">Nossa História</a>
      <a href="#">Cervejas</a>
      <a href="#">A Cervejaria</a>
      <a href="#">Eventos</a>
      <a href="#">Contato</a>
    </nav>
    <div class="social"><span></span><span></span></div>
  </header>

  <div class="wheat-left" role="img" aria-label="Ears of wheat"></div>
  <div class="bottles" role="img" aria-label="Two amber beer bottles with labels and bottle caps"></div>

  <h1 class="heading-xl hero-title">Velmont</h1>
  <h2 class="heading-xl hero-sub">Cerveja Artesanal</h2>
  <p class="body-copy hero-copy">Lorem Ipsum is simply dummy text of the printing and typesetting industry. Lorem Ipsum has been the industry's standard dummy text ever since the 1500s, when an unknown printer took a galley of type and scrambled it to make a type specimen book. It has survived not only five centuries, but also the leap into electronic typesetting, remaining essentially unchanged. It was popularised in the 1960s with the release of Letraset sheets containing Lorem Ipsum passages, and more recently with desktop publishing software like Aldus PageMaker including versions of Lorem Ipsum.</p>
  <div class="hero-actions">
    <a class="more-link" href="#">More Detail &gt;</a>
    <span class="like-btn"><b>Like</b><i>54k</i></span>
  </div>

  <div class="video">
    <div class="video-frame" role="img" aria-label="Blurred glass of beer on a bar counter"></div>
    <svg class="play" viewBox="0 0 74 52"><polygon points="30,16 30,36 47,26" fill="#fff"/></svg>
    <div class="video-bar"><span>▶</span><span>0:00 / 5:22</span></div>
  </div>

  <div class="wheat-right" role="img" aria-label="Ears of wheat"></div>

  <h2 class="heading-xl feature-title">Velmont</h2>
  <h3 class="heading-xl feature-sub">Cerveja Artesanal</h3>
  <p class="body-copy feature-copy">Lorem Ipsum is simply dummy text of the printing and typesetting industry. Lorem Ipsum has been the industry's standard dummy text ever since the 1500s, when an unknown printer took a galley of type and scrambled it to make a type specimen book. It has survived not only five centuries, but also the leap into electronic typesetting, remaining essentially unchanged. It was popularised in the 1960s with the release.</p>
  <a class="more-link feature-more" href="#">More Detail &gt;</a>

  <div class="glasses" role="img" aria-label="Two glasses of foamy beer"></div>
  <h2 class="heading-xl contact-title">Contato</h2>
  <h3 class="label-title enquiry">Enquiry:</h3>
  <form class="enquiry-form">
    <label class="field name">Name</label>
    <label class="field email">Email</label>
    <label class="field comment">Comment</label>
  </form>

  <div class="contact-info">
    <h3 class="label-title">Address:</h3>
    <p>Lorem Ipsum is simply dummy text<br>the printing and typesetting industry.<br>Lorem Ipsum has been the industry</p>
    <h3 class="label-title">Tel:</h3>
    <p>1-555-0147-220</p>
    <h3 class="label-title">Email:</h3>
    <p>hello@velmont.mail</p>
  </div>

  <footer class="site-footer"><span class="copyright">Copyright © 2014 Velmont.</span></footer>
  <div class="bottle-cap" role="img" aria-label="Bottle cap"></div>
</body>
</html>
```